Brisk.to Landing Page Redesign Challenge - Help us pop and convert better!

** Update: We might not have been clear enough in our original messaging. We’re VERY open to changing the primary color from blue, we want a site that pops and has a good vibe for our audience (Creators, influencers). We originally chose blue as that is trust building, but I'd love to see some designs that show flare and flavor, with some really good contrasting colors with purple as a primary color... We'd love to see something in between https://clipvane.com and https://tallyform.app ... Again, our only caveat is orange cannot be a primary color because of a competitor.**

We built our current landing page fast — because PixelWave picked us to power the launch of his ArenaTrials show on Streamora Plus and we had to be ready overnight.

You can read the case study here:
https://brisk.to/app/blog/2025/05/08/pixelwave-streamora-plus-arena-trials-launch

Now that the dust has settled, we’re ready for a proper redesign — and we want to see your vision.

What we need:

A bold, vibrant color palette that feels fresh and fun — something that speaks to digital creators, influencers, and small businesses with 1–3 person marketing teams.

Our current main color is #3690C2, used by our mascot (Milo).

A full landing page redesign (desktop and mobile) in Figma that:

Clearly explains what Brisk.to does (link management + smart analytics for creators and marketers).

Builds trust and credibility using social proof and metrics.

Flows users toward conversion (signing up or starting a paid plan).

Is visually appealing and fun, without being overwhelming.

To submit:

Please send:

A hero section mockup.

Your proposed color palette (with hex codes).

A rough idea of how you’d structure the rest of the page.

The winning designer will deliver the full redesign in Figma.

BONUS: We’re considering inviting the winning designer to join our startup long-term, on a stock option package (no salary for now, we're building revenue first) as we grow what we believe will be the best link platform on the internet.

We're excited to see what you create!

*** GUIDANCE ***

Hero Section

Should include this Title and subtitle:

More Than a Short Link.
Brisk.to is your creative command center — shorten, track, and transform links that adapt over time.

Should include these bullet points are something close to it:

Unlimited links & QR codes
Link-in-bio + shortener, combined
Monitor Your Links
Conversion analytics included
Free trial — no card required

Trust Bar Text

30M+
Trusted by over 30 million people
1B+
Data points tracked — and counting
Real-time
Every click. Every view. Tracked in real-time

The rest of the text you can find on our current Landing Page at: https://brisk.to

Feel free to create a new account and play around with the site, to get screen shots and such.

Target Market(s)

Creators, Influencers and SMBs with 1-3 person marketing team

Industry/Entity Type

Social, Marketing

Number of Pages Required

1 page

Font styles to use
Other font styles liked:
• Logo is Belotta, Main text is Lato

Colors
0054AA
0677BA
7BADD7
CADEEF
E8F1F8
6B429C
8869AF
B7A5CE
E3DAEB
F3F0F8

Requirements
Must have
• Equivalent sections as my current page,
Nice to have
• Trust Bar - I have an example attached with my latest attempt to make the site look better.
Should not have
• Orange, our biggest competitor uses orange heavily.

```html
<!DOCTYPE html>
<html lang="en">
<head>
<meta charset="utf-8">
<title>Brisk.to — More Than a Short Link</title>
<link rel="stylesheet" href="https://fonts.googleapis.com/css2?family=Poppins:wght@500;600;700;800&family=Lato:wght@400;700;900&display=swap">
<style>
:root{
  --purple:#7a3fd1;
  --purple-deep:#6b429c;
  --purple-mid:#8869af;
  --purple-soft:#b7a5ce;
  --lilac:#e3daeb;
  --lilac-pale:#f3f0f8;
  --teal:#22b8a4;
  --ink:#1d1a2e;
  --ink-soft:#4a4660;
  --muted:#8a87a0;
  --line:#e7e4ef;
  --white:#ffffff;
  --night:#1c1a30;
  --night-2:#25223d;
}
*{box-sizing:border-box;margin:0;padding:0}
html,body{width:1200px;height:4916px;overflow:hidden}
body{font-family:"Lato",sans-serif;color:var(--ink);background:var(--white);font-size:14px;line-height:1.5}
h1,h2,h3,h4,.brand,.stat-num,.price{font-family:"Poppins",sans-serif}
a{color:inherit;text-decoration:none}
ul{list-style:none}
.wrap{width:1080px;margin:0 auto;position:relative}
.accent{color:var(--purple)}
.accent-teal{color:var(--teal)}
.btn{display:inline-block;font-family:"Lato",sans-serif;font-weight:700;font-size:13px;border-radius:8px;padding:11px 22px;border:1.5px solid transparent;white-space:nowrap}
.btn-teal{background:var(--teal);color:var(--white)}
.btn-ghost{border-color:rgba(255,255,255,.8);color:var(--white)}
.btn-outline{border-color:var(--ink);color:var(--ink)}
.check{width:16px;height:16px;flex:none}

/* Hero */
.hero{height:540px;background:linear-gradient(120deg,#7b2fe0 0%,#a447e6 38%,#c25ed8 55%,#5fb6dc 82%,#3ec7c9 100%);color:var(--white);position:relative;overflow:hidden}
.nav{display:flex;align-items:center;height:72px}
.brand{font-weight:800;font-size:22px;letter-spacing:-.3px}
.nav-links{display:flex;gap:30px;margin-left:auto;margin-right:auto;font-size:13px;font-weight:700}
.nav-actions{display:flex;align-items:center;gap:22px;font-size:13px;font-weight:700}
.hero-copy{position:absolute;left:0;top:82px;width:600px}
.hero h1{font-size:38px;font-weight:800;line-height:1.15;letter-spacing:-.5px;white-space:nowrap}
.hero h1 .pill{background:var(--white);color:var(--purple);padding:0 10px;border-radius:8px}
.hero-sub{margin-top:14px;font-size:15px;max-width:440px;opacity:.95}
.hero-list{margin-top:20px;display:grid;gap:9px;font-weight:700;font-size:14px}
.hero-list li{display:flex;align-items:center;gap:10px}
.hero-cta{margin-top:30px;display:flex;gap:14px}
.hero-art{position:absolute;right:40px;top:90px;width:400px;height:340px;border-radius:28px;background:radial-gradient(circle at 30% 30%,#f7d86a 0 14%,transparent 15%),linear-gradient(145deg,#f2b7ff 0%,#c15cf0 40%,#7c2fe0 75%,#4b1fa0 100%);transform:rotate(-6deg);box-shadow:0 30px 60px rgba(40,10,90,.35)}

/* Trust */
.trust{height:400px;padding-top:60px}
.stats{display:grid;grid-template-columns:repeat(3,1fr);gap:26px}
.stat{background:var(--lilac-pale);border:1px solid var(--lilac);border-radius:16px;padding:24px 28px;height:160px;text-align:center}
.stat-icon{width:42px;height:42px;border-radius:12px;background:var(--purple-mid);display:grid;place-items:center;margin:0 auto 12px}
.stat-num{font-size:30px;font-weight:700;color:var(--purple);line-height:1}
.stat-label{margin-top:8px;color:var(--ink-soft);font-size:13px}
.logos{margin-top:56px;display:flex;justify-content:space-between;align-items:center;padding:0 20px}
.logo-name{font-family:"Lato",sans-serif;font-weight:900;font-size:24px;color:#8e8ba3}

/* Why */
.why{height:420px;padding-top:36px;text-align:center}
.section-title{font-size:32px;font-weight:700;letter-spacing:-.3px}
.why-cards{margin-top:48px;display:grid;grid-template-columns:repeat(3,1fr);gap:26px;align-items:start}
.why-card{border:1px solid var(--line);border-radius:16px;padding:26px 26px 28px;background:var(--white)}
.why-card.featured{border-color:var(--purple-soft);box-shadow:0 18px 40px rgba(107,66,156,.16);margin-top:-20px}
.why-icon{width:54px;height:54px;border-radius:50%;background:var(--ink);margin:0 auto 16px;display:grid;place-items:center}
.why-card.featured .why-icon{background:var(--purple)}
.why-card h3{font-size:16px;font-weight:600}
.why-card p{margin-top:8px;color:var(--muted);font-size:12.5px}

/* Case */
.case{height:380px;background:linear-gradient(100deg,#7b2fe0 0%,#9a3ee6 55%,#c16ae8 100%);color:var(--white);position:relative}
.case-copy{position:absolute;left:0;top:52px;width:520px}
.eyebrow{font-size:11px;font-weight:900;letter-spacing:1.6px;text-transform:uppercase;opacity:.85}
.case h2{margin-top:10px;font-size:25px;font-weight:700;line-height:1.25}
.case-copy p{margin-top:12px;font-size:13px;opacity:.9}
.case-list{margin-top:16px;display:grid;gap:8px;font-weight:700;font-size:13.5px}
.case-list li{display:flex;gap:10px;align-items:center}
.read-more{display:inline-block;margin-top:18px;font-weight:900;font-size:12px;letter-spacing:1px}
.case-shot{position:absolute;right:0;top:-10px;width:480px;height:330px;border-radius:14px;border:8px solid var(--white);background:linear-gradient(135deg,#2a1844 0%,#5b2a8f 45%,#1b1430 100%);box-shadow:0 24px 50px rgba(20,0,50,.4);transform:rotate(3deg)}

/* Features */
.features{height:500px;padding-top:50px;text-align:center}
.section-sub{margin:10px auto 0;max-width:540px;color:var(--muted);font-size:13px}
.tabs{margin:28px auto 0;display:flex;justify-content:space-between;width:760px;border-bottom:1px solid var(--line);font-weight:700;font-size:13px;color:var(--ink-soft)}
.tab{padding:10px 34px}
.tab.active{color:var(--purple);border-bottom:3px solid var(--purple)}
.feature-row{display:flex;text-align:left;margin-top:34px;gap:60px;align-items:flex-start}
.feature-copy{width:380px;padding-top:20px}
.feature-copy h3{font-size:28px;font-weight:700}
.feature-copy p{margin-top:10px;color:var(--muted);font-size:13px}
.feature-list{margin-top:18px;display:grid;gap:10px;font-weight:700;font-size:13.5px}
.feature-list li{display:flex;gap:10px;align-items:center}
.dash{flex:1;height:250px;border:2px solid var(--purple-soft);border-radius:14px;background:var(--white);box-shadow:0 16px 40px rgba(107,66,156,.14);padding:14px}

/* Testimonials */
.reviews{height:440px;background:linear-gradient(180deg,#f3f0f8 0%,#fbf9fd 100%);padding-top:56px;text-align:center}
.review-cards{margin-top:34px;display:grid;grid-template-columns:repeat(3,1fr);gap:26px;text-align:left}
.review{background:var(--white);border-radius:14px;padding:22px 24px;box-shadow:0 10px 30px rgba(60,30,110,.08);position:relative}
.review-head{display:flex;align-items:center;gap:12px}
.avatar{width:40px;height:40px;border-radius:50%;background:linear-gradient(135deg,var(--purple-soft),var(--purple-mid))}
.review-name{font-weight:900;font-size:13.5px}
.stars{color:#f3b63f;font-size:11px;letter-spacing:1px}
.quote{position:absolute;right:22px;top:16px;font-family:"Poppins",sans-serif;font-size:40px;line-height:1;color:var(--purple)}
.review p{margin-top:14px;font-size:12.5px;color:var(--ink-soft)}
.pager{margin-top:26px;display:flex;justify-content:center;align-items:center;gap:10px;color:var(--muted);font-size:12px}
.dot{width:7px;height:7px;border-radius:50%;background:var(--purple-soft)}
.dot.on{width:20px;border-radius:4px;background:var(--purple)}

/* Pricing */
.pricing{height:700px;padding-top:70px}
.pricing-head{display:flex;justify-content:space-between;align-items:flex-end}
.pricing-head p{margin-top:8px;color:var(--muted);font-size:13px;max-width:330px}
.toggle{display:flex;border:1px solid var(--line);border-radius:20px;padding:3px;font-size:11px;font-weight:900}
.toggle span{padding:6px 16px;border-radius:16px}
.toggle .on{background:var(--purple);color:var(--white)}
.plans{margin-top:40px;display:grid;grid-template-columns:1fr 1fr 1.05fr;gap:24px;align-items:end}
.plan{border:1px solid var(--line);border-radius:16px;padding:28px 26px;height:420px;display:flex;flex-direction:column}
.price{font-size:30px;font-weight:700}
.price small{font-size:12px;font-weight:500;color:var(--muted)}
.plan h4{font-size:17px;font-weight:600;margin-top:4px}
.plan-desc{font-size:12px;color:var(--muted);margin-top:6px}
.plan-list{margin-top:18px;display:grid;gap:10px;font-size:12.5px;color:var(--ink-soft)}
.plan-list li{display:flex;gap:10px;align-items:center}
.plan .btn{margin-top:auto;text-align:center;width:100%}
.plan.popular{background:var(--night);color:var(--white);border:none;height:460px;box-shadow:0 24px 50px rgba(28,26,48,.3)}
.plan.popular .plan-desc,.plan.popular .plan-list{color:#c9c5dc}
.badge{align-self:flex-start;background:var(--purple);color:var(--white);font-size:10px;font-weight:900;padding:4px 12px;border-radius:12px;margin-bottom:14px;letter-spacing:.5px}

/* FAQ */
.faq{height:500px;background:var(--night);color:var(--white);padding-top:70px}
.faq-grid{display:flex;gap:60px}
.faq-intro{width:360px;flex:none}
.faq-intro h2{font-size:32px;font-weight:700;line-height:1.2;white-space:nowrap}
.faq-intro h2 .accent{color:#b98cf5}
.faq-intro p{margin-top:16px;color:#b7b3cc;font-size:13px;max-width:330px}
.faq-list{flex:1}
.faq-item{display:flex;justify-content:space-between;align-items:center;padding:15px 4px;border-bottom:1px solid rgba(255,255,255,.12);font-size:13.5px;font-weight:700}
.faq-item.open{display:block;background:var(--white);color:var(--ink);border-radius:10px;padding:16px 18px;border:none;margin:8px 0}
.faq-item.open .faq-q{display:flex;justify-content:space-between}
.faq-item.open p{font-weight:400;color:var(--ink-soft);font-size:12.5px;margin-top:8px}
.chev{font-size:14px;opacity:.7}

/* Browsers */
.browsers{height:480px;padding-top:70px;text-align:center}
.browser-cards{margin-top:40px;display:grid;grid-template-columns:repeat(4,1fr);gap:24px}
.browser{border:1px solid var(--line);border-radius:16px;padding:28px 20px;box-shadow:0 8px 24px rgba(60,30,110,.06)}
.browser-mark{width:60px;height:60px;border-radius:50%;margin:0 auto 14px}
.browser h4{font-size:16px;font-weight:600}
.browser p{font-size:12px;color:var(--muted);margin-top:4px}
.browser .btn{margin-top:18px;padding:9px 24px;font-size:12px}
.browser .soon{margin-top:18px;font-size:12px;color:var(--muted);padding:9px 0}

/* CTA */
.cta{height:200px;background:linear-gradient(100deg,#7b2fe0 0%,#a447e6 60%,#c25ed8 100%);color:var(--white)}
.cta .wrap{display:flex;align-items:center;justify-content:space-between;height:200px}
.cta h2{font-size:32px;font-weight:700}
.cta p{font-size:14px;opacity:.9;margin-top:6px}
.cta-actions{display:flex;gap:14px}
.btn-white{background:var(--white);color:var(--purple)}

/* Footer */
.footer{height:356px;background:var(--night);color:var(--white);padding-top:60px}
.footer-grid{display:grid;grid-template-columns:2fr 1fr 1fr 1fr 1fr;gap:30px}
.socials{display:flex;gap:12px;margin-top:18px}
.social{width:26px;height:26px;border-radius:50%;background:var(--night-2);border:1px solid rgba(255,255,255,.2)}
.footer h5{font-family:"Lato",sans-serif;font-size:14px;font-weight:900;margin-bottom:12px}
.footer li{font-size:12.5px;color:#b7b3cc;margin-bottom:8px}
.copyright{margin-top:44px;padding-top:22px;border-top:1px solid rgba(255,255,255,.12);text-align:center;font-size:12px;color:#9b97b3}
</style>
</head>
<body>

<header class="hero">
  <div class="wrap">
    <nav class="nav">
      <span class="brand">Brisk.to</span>
      <ul class="nav-links"><li>Home</li><li>Features</li><li>Pricing</li><li>Case Studies</li><li>Blog</li></ul>
      <div class="nav-actions"><a>Log In</a><a class="btn btn-teal">Start Free Trial</a></div>
    </nav>
    <div class="hero-copy">
      <h1>More Than a <span class="pill">Short Link</span>.</h1>
      <p class="hero-sub">Brisk.to is your creative command center — shorten, track, and transform links that adapt over time.</p>
      <ul class="hero-list">
        <li><svg class="check" viewBox="0 0 16 16"><circle cx="8" cy="8" r="8" fill="#fff"/><path d="M4.5 8.2l2.2 2.2 4.8-4.8" stroke="#7a3fd1" stroke-width="2" fill="none"/></svg>Unlimited links &amp; QR codes</li>
        <li><svg class="check" viewBox="0 0 16 16"><circle cx="8" cy="8" r="8" fill="#fff"/><path d="M4.5 8.2l2.2 2.2 4.8-4.8" stroke="#7a3fd1" stroke-width="2" fill="none"/></svg>Link-in-bio + shortener, combined</li>
        <li><svg class="check" viewBox="0 0 16 16"><circle cx="8" cy="8" r="8" fill="#fff"/><path d="M4.5 8.2l2.2 2.2 4.8-4.8" stroke="#7a3fd1" stroke-width="2" fill="none"/></svg>Monitor Your Links</li>
        <li><svg class="check" viewBox="0 0 16 16"><circle cx="8" cy="8" r="8" fill="#fff"/><path d="M4.5 8.2l2.2 2.2 4.8-4.8" stroke="#7a3fd1" stroke-width="2" fill="none"/></svg>Conversion analytics included</li>
        <li><svg class="check" viewBox="0 0 16 16"><circle cx="8" cy="8" r="8" fill="#fff"/><path d="M4.5 8.2l2.2 2.2 4.8-4.8" stroke="#7a3fd1" stroke-width="2" fill="none"/></svg>Free trial — no card required</li>
      </ul>
      <div class="hero-cta"><a class="btn btn-teal">Start Your Trial</a><a class="btn btn-ghost">See How It Works in Action</a></div>
    </div>
    <div class="hero-art" role="img" aria-label="Playful 3D browser window with floating analytics charts and link cards"></div>
  </div>
</header>

<section class="trust">
  <div class="wrap">
    <div class="stats">
      <div class="stat"><div class="stat-icon"><svg width="22" height="22" viewBox="0 0 22 22"><circle cx="8" cy="7" r="3.5" fill="#fff"/><circle cx="15" cy="8" r="3" fill="#fff" opacity=".7"/><path d="M1.5 19c0-4 3-6 6.5-6s6.5 2 6.5 6z" fill="#fff"/></svg></div><div class="stat-num">30M+</div><div class="stat-label">Trusted by over 30 million people</div></div>
      <div class="stat"><div class="stat-icon"><svg width="22" height="22" viewBox="0 0 22 22"><rect x="3" y="11" width="4" height="8" fill="#fff"/><rect x="9" y="6" width="4" height="13" fill="#fff"/><rect x="15" y="3" width="4" height="16" fill="#fff"/></svg></div><div class="stat-num">1B+</div><div class="stat-label">Data points tracked — and counting</div></div>
      <div class="stat"><div class="stat-icon"><svg width="22" height="22" viewBox="0 0 22 22"><circle cx="11" cy="11" r="8" stroke="#fff" stroke-width="2" fill="none"/><path d="M11 6v5l3 3" stroke="#fff" stroke-width="2" fill="none"/></svg></div><div class="stat-num">Real-time</div><div class="stat-label">Every click. Every view. Tracked in real-time</div></div>
    </div>
    <div class="logos">
      <span class="logo-name">Logoform</span>
      <span class="logo-name">PixelWave</span>
      <span class="logo-name">Streamora Plus</span>
      <span class="logo-name">Logoform</span>
      <span class="logo-name">Logoform</span>
    </div>
  </div>
</section>

<section class="why">
  <div class="wrap">
    <h2 class="section-title">Why Creators Choose <span class="accent">Brisk.to</span></h2>
    <div class="why-cards">
      <div class="why-card"><div class="why-icon"><svg width="24" height="24" viewBox="0 0 24 24"><path d="M10 14a4 4 0 0 0 5.6 0l3-3a4 4 0 0 0-5.6-5.6l-1 1M14 10a4 4 0 0 0-5.6 0l-3 3a4 4 0 0 0 5.6 5.6l1-1" stroke="#fff" stroke-width="2" fill="none" stroke-linecap="round"/></svg></div><h3>Unlimited Links &amp; QR Codes</h3><p>No caps. No throttling. Create as many as you need — whenever you need them.</p></div>
      <div class="why-card featured"><div class="why-icon"><svg width="24" height="24" viewBox="0 0 24 24"><rect x="6" y="3" width="12" height="18" rx="2" stroke="#fff" stroke-width="2" fill="none"/><path d="M9 8h6M9 12h6M9 16h4" stroke="#fff" stroke-width="2"/></svg></div><h3>Short Links + Link-in-Bio</h3><p>One platform to manage both — keep everything streamlined under one smart dashboard.</p></div>
      <div class="why-card"><div class="why-icon"><svg width="24" height="24" viewBox="0 0 24 24"><path d="M4 18l5-6 4 3 7-9" stroke="#fff" stroke-width="2" fill="none" stroke-linecap="round"/></svg></div><h3>Built-In Conversion Tracking</h3><p>See clicks, conversions, and traffic in real time — without a third-party integration.</p></div>
    </div>
  </div>
</section>

<section class="case">
  <div class="wrap">
    <div class="case-copy">
      <span class="eyebrow">Case Study</span>
      <h2>Powering the Launch of Arena Trials<br>on Streamora Plus</h2>
      <p>PixelWave trusted Brisk.to to handle every link for the premiere — fast, scalable and tracked end to end.</p>
      <ul class="case-list">
        <li><svg class="check" viewBox="0 0 16 16"><circle cx="8" cy="8" r="8" fill="#fff"/><path d="M4.5 8.2l2.2 2.2 4.8-4.8" stroke="#7a3fd1" stroke-width="2" fill="none"/></svg>Shortened Thousands Of Campaign Links In Real Time</li>
        <li><svg class="check" viewBox="0 0 16 16"><circle cx="8" cy="8" r="8" fill="#fff"/><path d="M4.5 8.2l2.2 2.2 4.8-4.8" stroke="#7a3fd1" stroke-width="2" fill="none"/></svg>Handled 300M+ Link Views During Premiere Week</li>
        <li><svg class="check" viewBox="0 0 16 16"><circle cx="8" cy="8" r="8" fill="#fff"/><path d="M4.5 8.2l2.2 2.2 4.8-4.8" stroke="#7a3fd1" stroke-width="2" fill="none"/></svg>Launch-Ready In Under 12 Hours</li>
      </ul>
      <a class="read-more">READ MORE →</a>
    </div>
    <div class="case-shot" role="img" aria-label="Streaming show landing page screenshot for the Arena Trials premiere"></div>
  </div>
</section>

<section class="features">
  <div class="wrap">
    <h2 class="section-title">Everything You Need in <span class="accent">One Place</span></h2>
    <p class="section-sub">From dynamic short links to advanced analytics, Brisk.to gives you total control. Explore the tools trusted by top creators and growing brands — all in one seamless platform.</p>
    <div class="tabs"><span class="tab active">Analytics</span><span class="tab">QR Codes</span><span class="tab">Smart Links</span><span class="tab">Security</span></div>
    <div class="feature-row">
      <div class="feature-copy">
        <h3>Real-Time Click <span class="accent-teal">Tracking</span></h3>
        <p>See exactly who's clicking, where, and from where. No spreadsheets, no delays — just clean, actionable data built for creators and marketers.</p>
        <ul class="feature-list">
          <li><svg class="check" viewBox="0 0 16 16"><circle cx="8" cy="8" r="8" fill="#7a3fd1"/><path d="M4.5 8.2l2.2 2.2 4.8-4.8" stroke="#fff" stroke-width="2" fill="none"/></svg>Time-Based Trends</li>
          <li><svg class="check" viewBox="0 0 16 16"><circle cx="8" cy="8" r="8" fill="#7a3fd1"/><path d="M4.5 8.2l2.2 2.2 4.8-4.8" stroke="#fff" stroke-width="2" fill="none"/></svg>Geo Tracking</li>
          <li><svg class="check" viewBox="0 0 16 16"><circle cx="8" cy="8" r="8" fill="#7a3fd1"/><path d="M4.5 8.2l2.2 2.2 4.8-4.8" stroke="#fff" stroke-width="2" fill="none"/></svg>Conversion Metrics</li>
        </ul>
      </div>
      <div class="dash">
        <svg width="100%" height="220" viewBox="0 0 600 220" preserveAspectRatio="none">
          <rect x="0" y="0" width="600" height="26" rx="6" fill="#f3f0f8"/>
          <rect x="12" y="8" width="110" height="10" rx="5" fill="#b7a5ce"/>
          <g stroke="#eee" stroke-width="1"><line x1="20" y1="60" x2="400" y2="60"/><line x1="20" y1="110" x2="400" y2="110"/><line x1="20" y1="160" x2="400" y2="160"/><line x1="20" y1="205" x2="400" y2="205"/></g>
          <polyline points="20,170 70,150 120,160 170,110 220,125 270,80 320,95 370,60 400,70" fill="none" stroke="#7a3fd1" stroke-width="3"/>
          <polyline points="20,190 70,180 120,175 170,160 220,165 270,140 320,150 370,120 400,125" fill="none" stroke="#22b8a4" stroke-width="3"/>
          <circle cx="500" cy="100" r="55" fill="none" stroke="#e3daeb" stroke-width="22"/>
          <circle cx="500" cy="100" r="55" fill="none" stroke="#7a3fd1" stroke-width="22" stroke-dasharray="220 346" transform="rotate(-90 500 100)"/>
          <circle cx="500" cy="100" r="55" fill="none" stroke="#22b8a4" stroke-width="22" stroke-dasharray="70 346" stroke-dashoffset="-220" transform="rotate(-90 500 100)"/>
          <g fill="#b7a5ce"><rect x="440" y="180" width="20" height="25"/><rect x="470" y="170" width="20" height="35"/><rect x="500" y="160" width="20" height="45" fill="#7a3fd1"/><rect x="530" y="175" width="20" height="30"/></g>
        </svg>
      </div>
    </div>
  </div>
</section>

<section class="reviews">
  <div class="wrap">
    <h2 class="section-title">Loved by Creators, <span class="accent">Trusted by Teams</span></h2>
    <p class="section-sub">From solo influencers to small brands, Brisk.to powers the world's most creative marketers. Here's what our users have to say.</p>
    <div class="review-cards">
      <div class="review"><span class="quote">“</span><div class="review-head"><div class="avatar"></div><div><div class="review-name">Jordan Ellis</div><div class="stars">★★★★★</div></div></div><p>Brisk.to made sharing my drops so simple. One dashboard, every link, and I finally see which posts really drive my sales every week.</p></div>
      <div class="review"><span class="quote">“</span><div class="review-head"><div class="avatar"></div><div><div class="review-name">Samir Hale</div><div class="stars">★★★★★</div></div></div><p>We swapped three tools for one. Our tiny team now tracks every campaign click in real time and reports results in minutes, not days.</p></div>
      <div class="review"><span class="quote">“</span><div class="review-head"><div class="avatar"></div><div><div class="review-name">Alexa Dunn</div><div class="stars">★★★★★</div></div></div><p>The link-in-bio page looks great and the QR codes just work. Setup took five minutes and my audience noticed the cleaner look.</p></div>
    </div>
    <div class="pager"><span>‹</span><span class="dot"></span><span class="dot"></span><span class="dot on"></span><span class="dot"></span><span class="dot"></span><span>›</span></div>
  </div>
</section>

<section class="pricing">
  <div class="wrap">
    <div class="pricing-head">
      <div><h2 class="section-title">Plans &amp; <span class="accent">Pricing</span></h2><p>Whether your time saving automation needs are large or small, we're here to help you scale.</p></div>
      <div class="toggle"><span class="on">MONTHLY</span><span>YEARLY</span></div>
    </div>
    <div class="plans">
      <div class="plan">
        <div class="price">$0 <small>/month</small></div><h4>New users</h4><p class="plan-desc">Explore the basics of link management.</p>
        <ul class="plan-list">
          <li><svg class="check" viewBox="0 0 16 16"><circle cx="8" cy="8" r="8" fill="#e3daeb"/><path d="M4.5 8.2l2.2 2.2 4.8-4.8" stroke="#7a3fd1" stroke-width="2" fill="none"/></svg>Short Links Free</li>
          <li><svg class="check" viewBox="0 0 16 16"><circle cx="8" cy="8" r="8" fill="#e3daeb"/><path d="M4.5 8.2l2.2 2.2 4.8-4.8" stroke="#7a3fd1" stroke-width="2" fill="none"/></svg>5 Premium Apps</li>
          <li><svg class="check" viewBox="0 0 16 16"><circle cx="8" cy="8" r="8" fill="#e3daeb"/><path d="M4.5 8.2l2.2 2.2 4.8-4.8" stroke="#7a3fd1" stroke-width="2" fill="none"/></svg>Basic Analytics</li>
        </ul>
        <a class="btn btn-outline">Choose Plan</a>
      </div>
      <div class="plan">
        <div class="price">$5 <small>/month</small></div><h4>Individual pros</h4><p class="plan-desc">Advanced tools for solo creators ready to grow.</p>
        <ul class="plan-list">
          <li><svg class="check" viewBox="0 0 16 16"><circle cx="8" cy="8" r="8" fill="#e3daeb"/><path d="M4.5 8.2l2.2 2.2 4.8-4.8" stroke="#7a3fd1" stroke-width="2" fill="none"/></svg>Unlimited Links</li>
          <li><svg class="check" viewBox="0 0 16 16"><circle cx="8" cy="8" r="8" fill="#e3daeb"/><path d="M4.5 8.2l2.2 2.2 4.8-4.8" stroke="#7a3fd1" stroke-width="2" fill="none"/></svg>Custom QR Codes</li>
          <li><svg class="check" viewBox="0 0 16 16"><circle cx="8" cy="8" r="8" fill="#e3daeb"/><path d="M4.5 8.2l2.2 2.2 4.8-4.8" stroke="#7a3fd1" stroke-width="2" fill="none"/></svg>Link-in-Bio Page</li>
          <li><svg class="check" viewBox="0 0 16 16"><circle cx="8" cy="8" r="8" fill="#e3daeb"/><path d="M4.5 8.2l2.2 2.2 4.8-4.8" stroke="#7a3fd1" stroke-width="2" fill="none"/></svg>Shared Workspace</li>
        </ul>
        <a class="btn btn-outline">Choose Plan</a>
      </div>
      <div class="plan popular">
        <span class="badge">MOST POPULAR</span>
        <div class="price">$19 <small>/month</small></div><h4>Teams &amp; SMBs</h4><p class="plan-desc">Everything small marketing teams need to scale.</p>
        <ul class="plan-list">
          <li><svg class="check" viewBox="0 0 16 16"><circle cx="8" cy="8" r="8" fill="#22b8a4"/><path d="M4.5 8.2l2.2 2.2 4.8-4.8" stroke="#fff" stroke-width="2" fill="none"/></svg>Multi-User Seats</li>
          <li><svg class="check" viewBox="0 0 16 16"><circle cx="8" cy="8" r="8" fill="#22b8a4"/><path d="M4.5 8.2l2.2 2.2 4.8-4.8" stroke="#fff" stroke-width="2" fill="none"/></svg>Unlimited Premium Apps</li>
          <li><svg class="check" viewBox="0 0 16 16"><circle cx="8" cy="8" r="8" fill="#22b8a4"/><path d="M4.5 8.2l2.2 2.2 4.8-4.8" stroke="#fff" stroke-width="2" fill="none"/></svg>Unlimited Smart Links</li>
          <li><svg class="check" viewBox="0 0 16 16"><circle cx="8" cy="8" r="8" fill="#22b8a4"/><path d="M4.5 8.2l2.2 2.2 4.8-4.8" stroke="#fff" stroke-width="2" fill="none"/></svg>Advanced Admin</li>
          <li><svg class="check" viewBox="0 0 16 16"><circle cx="8" cy="8" r="8" fill="#22b8a4"/><path d="M4.5 8.2l2.2 2.2 4.8-4.8" stroke="#fff" stroke-width="2" fill="none"/></svg>Custom Domains</li>
        </ul>
        <a class="btn btn-teal">Choose Plan</a>
      </div>
    </div>
  </div>
</section>

<section class="faq">
  <div class="wrap faq-grid">
    <div class="faq-intro">
      <h2>Got Questions?<br>We've <span class="accent">Got Answers.</span></h2>
      <p>Here are the most common questions creators and marketers ask about Brisk.to. Still curious? Reach out anytime.</p>
    </div>
    <div class="faq-list">
      <div class="faq-item">Is Brisk.to free to use?<span class="chev">⌄</span></div>
      <div class="faq-item open"><div class="faq-q">What makes Brisk.to different from other link shorteners?<span class="chev">⌃</span></div><p>We're built specifically for creators and marketers — with bio pages, analytics, smart redirects, and real-time insights.</p></div>
      <div class="faq-item">Can I use Brisk.to for my brand or business?<span class="chev">⌄</span></div>
      <div class="faq-item">Do I get analytics with the free plan?<span class="chev">⌄</span></div>
      <div class="faq-item">What happens when I hit link limits?<span class="chev">⌄</span></div>
      <div class="faq-item">Do you support custom domains?<span class="chev">⌄</span></div>
    </div>
  </div>
</section>

<section class="browsers">
  <div class="wrap">
    <h2 class="section-title"><span class="accent">Brisk.to</span> on Every Browser</h2>
    <p class="section-sub">Work the way you want. Our browser extensions make it effortless to shorten and track links — right from your toolbar.</p>
    <div class="browser-cards">
      <div class="browser"><div class="browser-mark" style="background:#f0c24a"></div><h4>Corvid</h4><p>Available on the Web Store</p><a class="btn btn-teal">Install Now</a></div>
      <div class="browser"><div class="browser-mark" style="background:#b06ad8"></div><h4>Lumen</h4><p>Fast, privacy-first setup</p><a class="btn btn-teal">Install Now</a></div>
      <div class="browser"><div class="browser-mark" style="background:#3ec7d6"></div><h4>Ridgeway</h4><p>Desktop-native support</p><a class="btn btn-teal">Install Now</a></div>
      <div class="browser"><div class="browser-mark" style="background:#5a8fe0"></div><h4>Voyage</h4><p>Coming soon...</p><div class="soon">Stay tuned</div></div>
    </div>
  </div>
</section>

<section class="cta">
  <div class="wrap">
    <div><h2>Ready To Upgrade Your Link Game?</h2><p>Start creating, tracking, and transforming your links today — no credit card required.</p></div>
    <div class="cta-actions"><a class="btn btn-ghost">Talk to Sales</a><a class="btn btn-white">Start Free Trial</a></div>
  </div>
</section>

<footer class="footer">
  <div class="wrap">
    <div class="footer-grid">
      <div><span class="brand">Brisk.to</span><div class="socials"><span class="social"></span><span class="social"></span><span class="social"></span></div></div>
      <div><h5>Product</h5><ul><li>Features</li><li>Pricing</li><li>QR Codes</li><li>Link in Bio</li><li>Smart Analytics</li></ul></div>
      <div><h5>Resources</h5><ul><li>Blog</li><li>Case Studies</li><li>Help Center</li><li>API Docs</li></ul></div>
      <div><h5>Company</h5><ul><li>About Us</li><li>Careers</li><li>Contact Us</li></ul></div>
      <div><h5>Legal</h5><ul><li>Terms of Service</li><li>Privacy Policy</li><li>Cookies</li></ul></div>
    </div>
    <p class="copyright">Copyright © 2025 Brisk.to | All Rights Reserved.</p>
  </div>
</footer>

</body>
</html>
```